New Branding Business Card Design

Redesign business card according to new branding update.

** The design received so far are single color + BLACK.
I'd encourage designer to use different tones of blue / purple as described in the Designer Brief color palette

Target Market(s)

International

Industry/Entity Type

Medical Equipment

Contact Information for Business Card

Logo on one side (Designer can decide if they want to move certain info from the other side to save space)

Main body info (company name, individual name in both English and Chinese, contact info etc) on the other
Prefer a 'cleaner' layout - vs 'all over the place'
Prefer flush left alignment

Font styles to use
Sans Serif

Requirements
Must have
• Key info
• (Company name (English)): VORAM (HK) Limited
• (Name (English)): Marcus L. Pryde
• (Credential): FCPA, FHKSI
• (Title): Founder, Managing Director & CEO
• For the following info, designers decide whether to use colon or no colon, stroke separator, or use icon gfx for T (for telephone fixed line, M for mobile etc.)
• T: +852 3517 VORAM / +852 3517 4062
• M: +852 6243 7719 / + 86 139 2745 3186
• E: marcus.l.pryde@voram-example.hk
Nice to have
• Depending on the space and spacing available designers can add or use fuller title and other info
• Title: Chairman of the Executive Committee, Founder, Managing Director & CEO
• (Name (Chinese)): 林書恒
Should not have
• One of our business entities a long company name that cannot be broken into 2 lines
• makes vertical implementation almost impossible

```html
<!DOCTYPE html>
<html lang="en">
<head>
<meta charset="utf-8">
<title>VORAM (HK) Limited — Business Card</title>
<link rel="stylesheet" href="https://fonts.googleapis.com/css2?family=Montserrat:wght@500;600;700;800&family=Noto+Sans+TC:wght@400&display=swap">
<style>
  :root {
    --backdrop: #2a2a2c;
    --purple-deep: #55288a;
    --purple-mid: #6a3a9e;
    --purple-light: #7d52ad;
    --purple-text: #5a2c8e;
    --purple-soft: #8457b8;
    --paper: #ffffff;
  }
  * { margin: 0; padding: 0; box-sizing: border-box; }
  html, body {
    width: 1200px; height: 1200px; overflow: hidden;
    background: var(--backdrop);
    font-family: "Montserrat", sans-serif;
  }
  .sheet {
    width: 1200px; height: 1200px;
    display: flex; flex-direction: column; align-items: center; justify-content: center;
    gap: 60px;
  }
  .card {
    width: 900px; height: 500px;
    border-radius: 22px;
    position: relative;
    overflow: hidden;
  }
  .card--front {
    background: linear-gradient(135deg, var(--purple-deep) 0%, var(--purple-mid) 60%, var(--purple-light) 100%);
    display: flex; align-items: center; justify-content: center;
  }
  .brand {
    display: flex; align-items: center; gap: 18px;
    font-weight: 700; letter-spacing: 0.04em; text-transform: uppercase;
  }
  .brand__mark { width: 34px; height: 34px; border-radius: 6px; }
  .card--front .brand { color: var(--paper); font-size: 40px; }
  .card--front .brand__mark { background: var(--paper); width: 40px; height: 40px; }

  .card--back { background: var(--paper); }
  .identity {
    position: absolute; left: 60px; top: 56px;
    color: var(--purple-text);
  }
  .identity__name { font-size: 30px; font-weight: 800; letter-spacing: 0.03em; text-transform: uppercase; }
  .identity__name-zh { font-family: "Noto Sans TC", sans-serif; font-weight: 400; text-transform: none; letter-spacing: 0.05em; font-size: 28px; }
  .identity__credential { font-size: 19px; font-weight: 700; margin-top: 4px; }
  .identity__title { font-size: 19px; font-weight: 600; color: var(--purple-soft); line-height: 1.4; margin-top: 6px; }

  .contact {
    position: absolute; left: 60px; bottom: 52px;
    list-style: none; color: var(--purple-text);
    font-size: 21px; font-weight: 600;
  }
  .contact__item { display: flex; align-items: center; gap: 14px; line-height: 1.55; }
  .contact__key {
    width: 26px; height: 26px; border-radius: 5px;
    background: var(--purple-mid); color: var(--paper);
    font-size: 16px; font-weight: 600;
    display: inline-flex; align-items: center; justify-content: center;
  }
  .card--back .brand {
    position: absolute; right: 60px; top: 250px;
    color: var(--purple-mid); font-size: 28px;
  }
  .card--back .brand__mark { background: var(--purple-mid); }
</style>
</head>
<body>
<main class="sheet">
  <section class="card card--front" aria-label="Card front">
    <div class="brand"><span class="brand__mark"></span><span>VORAM (HK) Limited</span></div>
  </section>

  <section class="card card--back" aria-label="Card back">
    <div class="identity">
      <h1 class="identity__name">Marcus L. Pryde <span class="identity__name-zh">/ 林書恒</span></h1>
      <p class="identity__credential">FCPA, FHKSI</p>
      <p class="identity__title">Chairman of the Executive Committee<br>Founder, Managing Director &amp; CEO</p>
    </div>

    <ul class="contact">
      <li class="contact__item"><span class="contact__key">P</span>+852 3517 VORAM / +852 3517 4062</li>
      <li class="contact__item"><span class="contact__key">M</span>+852 6243 7719 / + 86 139 2745 3186</li>
      <li class="contact__item"><span class="contact__key">E</span>marcus.l.pryde@voram-example.hk</li>
    </ul>

    <div class="brand"><span class="brand__mark"></span><span>VORAM (HK) Limited</span></div>
  </section>
</main>
</body>
</html>
```